The book is titled "DREAM BUILD SOAR with a VICTOR"
It is written by a psychologist who is a former world champion, Australian captain and qualified organizational psychologist.
I have added the components of my champion star.
The book should reflect the qualities of champions..
BOLD COLOURFUL

Target Market(s)

16 to 60 year athletes coaches and club administrators (from average to elite). Much of the book also crosses to being a champion in other fields

Requirements
Must have
• The title
Smaller font An expert guide with practical solutions
The star some where
The top of field momentum logo ( can be small in corner)
My name as R T Hollins (M Psych, World Champion)
Bold Font biggest for Champion (to be a...smaller)

Can you please add
Player Team Coach Leader CEO

Like my name at the bottom

Colourful (can be fluoro)
Need A5 (main book) and A4 options for some schools who photocopy.
Nice to have
• Spine the book is 250 pages
Back design.. just colours or you can put the star there

```html
<!DOCTYPE html>
<html lang="en">
<head>
<meta charset="utf-8">
<title>Dream Build Soar with a Victor – Cover Spread</title>
<link rel="stylesheet" href="https://fonts.googleapis.com/css2?family=Lobster+Two:wght@700&family=Arimo:wght@400&family=Roboto+Condensed:wght@400&family=Crete+Round&display=swap">
<style>
  :root {
    --purple-cover: #a7429c;
    --pink: #e8308a;
    --teal: #1f9bbd;
    --violet: #7a3a96;
    --orange: #f7941d;
    --red: #e5213f;
    --navy: #1f5aa6;
    --ink: #333333;
    --white: #ffffff;
    --star-pink: #f29bc4;
    --star-yellow: #f4ec3b;
    --star-red: #e5283a;
    --star-blue: #3b9ad6;
    --badge-salmon: #f08a7e;
  }
  * { box-sizing: border-box; margin: 0; padding: 0; }
  html, body { width: 1200px; height: 814px; overflow: hidden; background: var(--white); }
  .spread { position: relative; width: 1200px; height: 814px; overflow: hidden; }

  /* Back cover */
  .back-cover {
    position: absolute; left: 0; top: 0; width: 567px; height: 814px;
    background: var(--purple-cover);
  }
  .back-copy {
    position: absolute; left: 42px; top: 74px; width: 484px;
    font-family: "Arimo", Arial, sans-serif; font-size: 12.6px; line-height: 21px;
    color: var(--white); text-align: justify;
  }
  .back-copy p { margin-bottom: 14px; }
  .back-star-art {
    float: left; width: 160px; height: 150px; margin: -36px 14px 6px -14px;
    border-radius: 50%;
    background: radial-gradient(circle at 50% 50%, var(--star-red) 0%, var(--star-pink) 40%, rgba(244,236,59,0.55) 62%, rgba(167,66,156,0) 72%);
  }

  /* Spine */
  .spine {
    position: absolute; left: 567px; top: 0; width: 50px; height: 814px;
    background: var(--purple-cover);
  }
  .spine-title {
    position: absolute; left: 50%; top: 132px; transform-origin: 0 0;
    transform: rotate(90deg) translateY(-50%);
    white-space: nowrap; font-family: "Lobster Two", cursive; font-weight: 700; font-size: 30px;
  }
  .spine-author {
    position: absolute; left: 50%; top: 632px; transform-origin: 0 0;
    transform: rotate(90deg) translateY(-50%);
    white-space: nowrap; color: var(--white); text-align: center;
  }
  .spine-author .name { font-family: "Crete Round", serif; font-size: 18px; display: block; line-height: 20px; }
  .spine-author .cred { font-family: "Crete Round", serif; font-size: 8.5px; display: block; }

  /* Front cover */
  .front-cover {
    position: absolute; left: 617px; top: 0; width: 583px; height: 814px;
    background:
      radial-gradient(circle at 20% 8%, #f6c9d6 0%, rgba(246,201,214,0.35) 28%, rgba(255,255,255,0) 55%),
      radial-gradient(circle at 90% 85%, #eef0fb 0%, rgba(255,255,255,0) 45%),
      var(--white);
  }
  .badge-art {
    position: absolute; left: 48px; top: 36px; width: 156px; height: 156px; border-radius: 50%;
    background: radial-gradient(circle at 50% 50%, var(--badge-salmon) 0%, rgba(240,138,126,0.6) 45%, rgba(255,255,255,0) 72%);
  }
  .badge-label {
    position: absolute; left: 100px; top: 62px; width: 80px; height: 80px; border-radius: 50%;
    background: var(--violet); color: var(--white); text-align: center;
    font-family: "Roboto Condensed", Arial, sans-serif; font-size: 12px; line-height: 13px;
    display: flex; align-items: center; justify-content: center; padding: 6px;
  }
  .imprint {
    position: absolute; left: 468px; top: 34px; width: 86px; height: 76px; border-radius: 50%;
    background: var(--white); display: flex; align-items: center; justify-content: center;
    text-align: center; font-family: "Roboto Condensed", Arial, sans-serif; font-size: 11px;
    line-height: 12px; color: var(--navy); padding: 8px;
  }
  .hero-star-art {
    position: absolute; left: 291px; top: 114px; width: 204px; height: 188px; border-radius: 50%;
    background: radial-gradient(circle at 50% 50%, var(--star-red) 0%, var(--star-pink) 35%, rgba(244,236,59,0.6) 55%, rgba(59,154,214,0.35) 66%, rgba(255,255,255,0) 74%);
  }
  .title { position: absolute; left: 0; top: 0; font-family: "Lobster Two", cursive; font-weight: 700; }
  .title span { position: absolute; white-space: nowrap; line-height: 1; }
  .t-dream { left: 58px; top: 200px; font-size: 86px; color: var(--pink); }
  .t-build { left: 76px; top: 300px; font-size: 120px; color: var(--teal); }
  .t-soar { left: 76px; top: 414px; font-size: 120px; color: var(--violet); }
  .t-with { left: 322px; top: 468px; font-size: 56px; color: var(--orange); }
  .t-victor { left: 70px; top: 524px; font-size: 134px; color: var(--red); }
  .subtitle {
    position: absolute; left: 79px; top: 668px; font-family: "Roboto Condensed", Arial, sans-serif;
    font-size: 22px; letter-spacing: 0.6px; color: var(--ink);
  }
  .author { position: absolute; left: 0; width: 583px; top: 724px; text-align: center; color: var(--navy); font-family: "Crete Round", serif; }
  .author .name { display: block; font-size: 38px; line-height: 44px; }
  .author .cred { display: block; font-size: 15px; }
</style>
</head>
<body>
<div class="spread">
  <section class="back-cover">
    <div class="back-copy">
      <div class="back-star-art" role="img" aria-label="Multicoloured champion star illustration"></div>
      <p>Lorem ipsum dolor sit amet, consectetur adipiscing elit, sed do eiusmod tempor incididunt ut labore et dolore magna aliqua. Ut enim ad minim veniam, quis nostrud exercitation ullamco laboris nisi ut aliquip ex ea commodo consequat. Duis aute irure dolor in reprehenderit in voluptate velit esse cillum dolore eu fugiat nulla pariatur. Excepteur sint occaecat cupidatat non proident, sunt in culpa qui officia deserunt mollit anim id est laborum.</p>
      <p>Lorem ipsum dolor sit amet, consectetur adipiscing elit, sed do eiusmod tempor incididunt ut labore et dolore magna aliqua. Ut enim ad minim veniam, quis nostrud exercitation ullamco laboris nisi ut aliquip ex ea commodo consequat. Duis aute irure dolor in reprehenderit in voluptate velit esse cillum dolore eu fugiat nulla pariatur. Excepteur sint occaecat cupidatat non proident, sunt in culpa qui officia deserunt mollit anim id est laborum.</p>
      <p>Lorem ipsum dolor sit amet, consectetur adipiscing elit, sed do eiusmod tempor incididunt ut labore et dolore magna aliqua. Ut enim ad minim veniam, quis nostrud exercitation ullamco laboris nisi ut aliquip ex ea commodo consequat. Duis aute irure dolor in reprehenderit in voluptate velit esse cillum dolore eu fugiat nulla pariatur. Excepteur sint occaecat cupidatat non proident, sunt in culpa qui officia deserunt mollit anim id est laborum.</p>
      <p>Lorem ipsum dolor sit amet, consectetur adipiscing elit, sed do eiusmod tempor incididunt ut labore et dolore magna aliqua. Ut enim ad minim veniam, quis nostrud exercitation ullamco laboris nisi ut aliquip ex ea commodo consequat. Duis aute</p>
    </div>
  </section>

  <section class="spine">
    <div class="spine-title">
      <span style="color:var(--pink)">Dream</span>
      <span style="color:var(--star-yellow)">Build</span>
      <span style="color:var(--star-yellow)">Soar</span>
      <span style="color:var(--orange)">with a</span>
      <span style="color:var(--red)">Victor</span>
    </div>
    <div class="spine-author">
      <span class="name">R T Hollins</span>
      <span class="cred">(M Psych, World Champion)</span>
    </div>
  </section>

  <section class="front-cover">
    <div class="badge-art" role="img" aria-label="Glowing salmon star burst behind the series badge"></div>
    <div class="badge-label">top of field momentum</div>

    <div class="imprint">top of field momentum</div>

    <div class="hero-star-art" role="img" aria-label="Multicoloured champion star illustration"></div>

    <h1 class="title">
      <span class="t-dream">Dream</span>
      <span class="t-build">Build</span>
      <span class="t-soar">Soar</span>
      <span class="t-with">with a</span>
      <span class="t-victor">Victor</span>
    </h1>

    <p class="subtitle">An expert guide with practical solutions</p>

    <div class="author">
      <span class="name">R T Hollins</span>
      <span class="cred">(M Psych, World Champion)</span>
    </div>
  </section>
</div>
</body>
</html>
```